GLOW RIDGE 21 DAY Challange

looking to make a poster that needs to be 36" wide x24"tall design graphic . Check out the added file as it is a rough draft of the material I would like it to say.

Phone number 555-302-4418 www.rgchiropractic..com

Adults aged 25-45 high income adults needing to make changes in dies and lose weight

```html
<!DOCTYPE html>
<html lang="en">
<head>
<meta charset="utf-8">
<title>GLOW RIDGE 21 Day Challange</title>
<link rel="stylesheet" href="https://fonts.googleapis.com/css2?family=Amatic+SC:wght@700&family=Luckiest+Guy&family=Permanent+Marker&display=swap">
<style>
  :root {
    --ink: #111111;
    --white: #ffffff;
    --banner-yellow: #f4f03a;
    --burst-yellow: #f7ee2c;
    --sky-blue: #4aa8e8;
    --royal-blue: #2f58d6;
    --lime: #5fd82c;
    --panel: rgba(40, 42, 60, 0.78);
    --row: rgba(255, 255, 255, 0.82);
    --display: "Luckiest Guy", Impact, "Arial Black", sans-serif;
    --marker: "Permanent Marker", "Arial Black", Impact, sans-serif;
    --hand: "Amatic SC", "Arial Narrow", sans-serif;
  }
  * { margin: 0; padding: 0; box-sizing: border-box; }
  html, body { width: 1200px; height: 800px; overflow: hidden; background: var(--white); }
  .poster { position: relative; width: 1200px; height: 800px; overflow: hidden; font-family: var(--marker); }

  .scene-photo {
    position: absolute; inset: 0;
    background: linear-gradient(180deg, #2a2a22 0%, #4a4a36 14%, #6b7f4a 22%, #5f9a2e 30%, #6aa936 60%, #4d8a24 100%);
  }

  .brand-title {
    position: absolute; left: 22px; top: 4px;
    font-family: var(--hand); font-weight: 700;
    font-size: 112px; line-height: 1; color: var(--white); letter-spacing: 1px;
    white-space: nowrap;
  }
  .chevrons { position: absolute; left: 440px; top: 18px; }

  .challenge-banner {
    position: absolute; left: 540px; top: 14px; width: 680px; height: 96px;
    background: var(--banner-yellow);
    box-shadow: 6px 6px 0 var(--ink);
    transform: rotate(-1.2deg);
    display: flex; align-items: center; padding-left: 40px; gap: 16px;
    font-family: var(--display); font-size: 56px; line-height: 1; white-space: nowrap;
  }
  .challenge-banner .days { color: var(--sky-blue); }
  .challenge-banner .word { color: var(--lime); -webkit-text-stroke: 1.5px var(--ink); }

  .question-row {
    position: absolute; height: 52px; background: var(--row);
    display: flex; align-items: center; padding-left: 14px;
    font-size: 29px; color: var(--ink); letter-spacing: 1px; white-space: pre;
  }
  .question-mark {
    position: absolute; font-family: var(--display);
    font-size: 80px; line-height: 1; -webkit-text-stroke: 2px #3a3a3a;
  }
  .q-green { color: var(--lime); }
  .q-blue { color: var(--sky-blue); }

  .call-burst { position: absolute; left: 0; top: 490px; }
  .call-text {
    position: absolute; left: 40px; top: 544px; width: 620px; text-align: center;
    font-family: var(--display); line-height: 1.08; white-space: nowrap;
  }
  .call-text .headline { color: var(--royal-blue); font-size: 32px; }
  .call-text .phone { color: var(--lime); font-size: 34px; -webkit-text-stroke: 0.6px #2a6a10; }
  .call-text .web { color: var(--royal-blue); font-size: 28px; }

  .plan-panel {
    position: absolute; left: 710px; top: 492px; width: 490px; height: 308px;
    background: var(--panel); padding: 6px 0 0 10px; list-style: none;
  }
  .plan-panel li {
    display: flex; align-items: center; height: 49px; line-height: 49px;
    color: var(--white); font-size: 22px; letter-spacing: 0.5px; white-space: nowrap; overflow: hidden;
  }
  .plan-panel .initial { font-family: var(--hand); font-weight: 700; font-size: 48px; line-height: 1; margin-right: 4px; }

  .clinic-mark {
    position: absolute; left: 6px; top: 748px; width: 230px; height: 46px;
    background: var(--white); display: flex; align-items: center; gap: 8px; padding-left: 10px;
    font-family: var(--display); font-size: 15px; color: var(--royal-blue); white-space: nowrap;
  }
  .clinic-mark .dot { width: 14px; height: 14px; background: var(--royal-blue); flex: none; }
</style>
</head>
<body>
<main class="poster">
  <div class="scene-photo" role="img" aria-label="Photo of a woman in a blue track suit and white headband stretching her leg on a sunny grass sports field with trees behind"></div>

  <h1 class="brand-title">GLOW RIDGE</h1>

  <svg class="chevrons" width="120" height="100" viewBox="0 0 120 100" aria-hidden="true">
    <polygon points="0,0 30,0 70,50 30,100 0,100 40,50" fill="#4aa8e8"/>
    <polygon points="45,0 75,0 115,50 75,100 45,100 85,50" fill="#4aa8e8"/>
  </svg>

  <div class="challenge-banner"><span class="days">21 DAY</span><span class="word">CHALLANGE</span></div>

  <div class="question-row" style="left:0;top:160px;width:520px;">DO YOU HAVE ALLERGIES</div>
  <span class="question-mark q-green" style="left:472px;top:148px;">?</span>
  <div class="question-row" style="left:70px;top:224px;width:485px;">WANT  TO LOSE WEIGHT</div>
  <span class="question-mark q-blue" style="left:512px;top:214px;">?</span>
  <div class="question-row" style="left:0;top:292px;width:470px;">ALWAYS FEELING TIRED</div>
  <span class="question-mark q-green" style="left:424px;top:280px;">?</span>
  <div class="question-row" style="left:18px;top:358px;width:510px;">HAVE NECK OR BACK PAIN</div>
  <span class="question-mark q-blue" style="left:500px;top:348px;">?</span>
  <div class="question-row" style="left:34px;top:422px;width:588px;">HAVE EXCESS WATER WEIGHT</div>
  <span class="question-mark q-green" style="left:576px;top:412px;">?</span>

  <svg class="call-burst" width="700" height="230" viewBox="0 490 700 230" aria-hidden="true">
    <polygon fill="#f7ee2c" stroke="#111" stroke-width="3" points="660,605 617,618 645,637 591,642 601,667 541,663 532,690 473,678 446,705 392,686 350,710 308,686 254,705 227,678 168,690 159,663 99,667 109,642 55,637 83,618 40,605 83,592 55,573 109,568 99,543 159,547 168,520 227,532 254,505 308,524 350,500 392,524 446,505 473,532 532,520 541,547 601,543 591,568 645,573 617,592"/>
  </svg>
  <div class="call-text">
    <p class="headline">CALL TODAY FOR DETAILS!</p>
    <p class="phone">555-302-4418</p>
    <p class="web">www.rgchiropractic..com</p>
  </div>

  <ul class="plan-panel">
    <li><span class="initial">L</span>- LIVER DETOX SUPPLEMENTS</li>
    <li><span class="initial">O</span>- OMEGA 3 SUPPLEMENTS</li>
    <li><span class="initial">V</span>- VITAMIN D SUPPLEMENTS</li>
    <li><span class="initial">E</span>- EAT FRUITS + VEGETABLES</li>
    <li><span class="initial">K</span>- KEFIR HOMEMADE PROBIOTIC</li>
    <li><span class="initial">C</span>-CHIROPRACTIC ADJUSTMENTS</li>
  </ul>

  <div class="clinic-mark"><span class="dot"></span>RIDGELINE CHIROPRACTIC</div>
</main>
</body>
</html>
```